Pipeline management & construction company needs nice brochure

Red Mesa Engineering & Construction, LLC (www.redmesaec.example) is a company focused on the midstream oil and gas / pipeline business. We plan, route, design, manage, and construction pipelines and related facilities. We need a brochure to summarize our services as well as give a brief listing of projects completed/desired.

Industry/Entity Type

Construction

Font styles to use
Serif

```html
<!DOCTYPE html>
<html lang="en">
<head>
<meta charset="utf-8">
<title>Red Mesa Engineering &amp; Construction — Brochure Spread</title>
<link href="https://fonts.googleapis.com/css2?family=Lora:ital,wght@0,400;0,600;1,400&family=Lato:ital,wght@0,300;0,400;1,400&display=swap" rel="stylesheet">
<style>
  :root{
    --backdrop:#d6d6d6;
    --paper:#f4f4f4;
    --ink:#3a3a3a;
    --ink-soft:#666;
    --gold:#e8b92f;
    --gold-soft:#ecca63;
    --charcoal:#565658;
    --row-white:#ffffff;
  }
  *{box-sizing:border-box;margin:0;padding:0}
  html,body{width:1200px;height:927px;overflow:hidden;background:var(--backdrop)}
  .spread{position:absolute;left:50px;top:84px;width:1100px;height:760px;display:flex;box-shadow:0 8px 24px rgba(0,0,0,.18)}
  .page{position:relative;width:550px;height:760px;background:var(--paper);overflow:hidden}
  .page--left{background:linear-gradient(90deg,#f6f6f6 0%,#f4f4f4 88%,#e2e2e2 100%)}
  .page--right{background:linear-gradient(90deg,#dedede 0%,#f4f4f4 10%,#f4f4f4 100%)}

  .brand{position:absolute;top:26px;display:flex;align-items:center;gap:7px;font-family:'Lora',serif;font-weight:600;font-size:17px;color:var(--ink)}
  .brand__dot{width:18px;height:18px;border-radius:50%;background:var(--gold)}
  .page--left .brand{left:34px}
  .page--right .brand{right:34px}

  .hero{position:absolute;left:0;top:58px;width:550px;height:310px}
  .hero__text{position:absolute;left:70px;top:248px;width:430px;font-family:'Lora',serif;font-style:italic;font-size:10.5px;line-height:1.45;color:var(--ink)}

  .services__title{position:absolute;left:92px;top:392px;font-family:'Lora',serif;font-size:30px;color:var(--ink-soft);font-weight:400}
  .service{position:absolute;font-family:'Lora',serif}
  .service__icon{display:block;width:26px;height:26px;margin-bottom:6px}
  .service__name{font-size:12px;letter-spacing:.3px;color:var(--ink);text-transform:uppercase}
  .service__list{list-style:none;margin-top:4px;font-family:'Lato',sans-serif;font-weight:300;font-size:11.5px;color:var(--ink);line-height:1.6}
  .service__list li::before{content:"";display:inline-block;width:5px;height:5px;border-radius:50%;background:var(--gold);margin-right:7px;vertical-align:middle}

  .showcase{position:absolute;left:0;top:70px;width:550px;height:340px}
  .showcase__title{position:absolute;left:56px;top:112px;font-family:'Lora',serif;font-style:italic;font-size:28px;color:var(--gold)}
  .shot{position:absolute;top:178px;width:122px}
  .shot__photo{display:block;width:122px;height:118px}
  .shot__caption{background:var(--gold-soft);height:50px;padding:8px 8px;font-family:'Lato',sans-serif;font-weight:300;font-size:10px;color:var(--ink);line-height:1.3}

  .projects{position:absolute;left:52px;width:448px}
  .projects__heading{font-family:'Lora',serif;font-size:13px;color:var(--ink);margin-bottom:4px}
  .projects__row{padding:2px 8px;height:22px;font-family:'Lato',sans-serif;font-size:7.5px;line-height:1.25;color:var(--ink)}
  .projects__row:nth-child(odd){background:var(--gold-soft)}
  .projects__row:nth-child(even){background:var(--row-white)}
  .projects__row em{display:block;font-style:italic}
</style>
</head>
<body>
<main class="spread">

  <section class="page page--left">
    <div class="brand"><span class="brand__dot"></span>Red Mesa</div>

    <svg class="hero" viewBox="0 0 550 310" role="img" aria-label="Photo of a pipeline right-of-way cut through a pine forest with pipe sections along the trench">
      <defs>
        <linearGradient id="forest" x1="0" y1="0" x2="0" y2="1">
          <stop offset="0" stop-color="#4f6b3a"/>
          <stop offset=".55" stop-color="#7a6a4a"/>
          <stop offset="1" stop-color="#a86a3e"/>
        </linearGradient>
      </defs>
      <path d="M0 0 H550 V200 Q300 170 0 235 Z" fill="url(#forest)"/>
      <path d="M0 235 Q300 170 550 200 V290 Q300 310 0 280 Z" fill="var(--gold)"/>
    </svg>
    <p class="hero__text">Red Mesa Engineering &amp; Construction, LLC (RMEC) is a specialty firm focused on the midstream oil and gas industry. The primary goal of RMEC is to assist midstream operating companies, as well as exploration and production companies, with the design and construction of their assets, specifically pipelines and related facilities.</p>

    <h2 class="services__title">Our Services</h2>

    <div class="service" style="left:120px;top:446px">
      <svg class="service__icon" viewBox="0 0 26 26" style="margin-left:48px"><circle cx="13" cy="13" r="13" fill="var(--charcoal)"/><rect x="8" y="7" width="10" height="13" rx="1" fill="var(--gold)"/></svg>
      <div class="service__name">Project Management</div>
      <ul class="service__list"><li>Project Management Consulting</li><li>“Cradle to Grave” Project Management</li><li>AFE/Budget Preparation</li><li>Detailed Design</li></ul>
    </div>

    <div class="service" style="left:96px;top:582px">
      <svg class="service__icon" viewBox="0 0 26 26" style="margin-left:48px"><circle cx="13" cy="13" r="13" fill="var(--charcoal)"/><path d="M7 19 L13 7 L19 19 Z" fill="var(--gold)"/></svg>
      <div class="service__name">Construction Management</div>
      <ul class="service__list"><li>Route Selection</li><li>ROW Acquisition</li><li>Survey Coordination</li><li>Constructability Reviews</li><li>QA/QC Inspection</li></ul>
    </div>

    <div class="service" style="left:342px;top:478px;text-align:center">
      <svg class="service__icon" viewBox="0 0 26 26" style="margin:0 auto 6px"><circle cx="13" cy="13" r="13" fill="var(--charcoal)"/><rect x="7" y="12" width="12" height="6" fill="var(--gold)"/></svg>
      <div class="service__name">LSTK / EPC Projects</div>
    </div>

    <div class="service" style="left:318px;top:552px">
      <svg class="service__icon" viewBox="0 0 26 26" style="margin-left:46px"><circle cx="13" cy="13" r="13" fill="var(--charcoal)"/><circle cx="13" cy="13" r="5" fill="var(--gold)"/></svg>
      <div class="service__name">Integrity Work</div>
      <ul class="service__list"><li>ILI Make Ready Assistance</li><li>Anomaly Repair</li><li>Hydrostatic Testing</li></ul>
    </div>

    <div class="service" style="left:318px;top:670px;text-align:center">
      <svg class="service__icon" viewBox="0 0 26 26" style="margin:0 auto 6px"><circle cx="13" cy="13" r="13" fill="var(--charcoal)"/><path d="M6 17 H20 L17 12 H9 Z" fill="var(--gold)"/></svg>
      <div class="service__name">Pipeline &amp; Facilities<br>Construction</div>
    </div>
  </section>

  <section class="page page--right">
    <div class="brand"><span class="brand__dot"></span>Red Mesa</div>

    <svg class="showcase" viewBox="0 0 550 340" aria-hidden="true">
      <path d="M0 0 H550 V235 Q300 195 0 250 Z" fill="var(--charcoal)"/>
    </svg>
    <h2 class="showcase__title">Completed Projects</h2>

    <figure class="shot" style="left:50px">
      <svg class="shot__photo" viewBox="0 0 122 118" role="img" aria-label="Photo of a sideboom lowering 10-inch pipe into a trench"><defs><linearGradient id="sky1" x1="0" y1="0" x2="0" y2="1"><stop offset="0" stop-color="#8fb4d6"/><stop offset=".6" stop-color="#b9a98a"/><stop offset="1" stop-color="#7d6c55"/></linearGradient></defs><rect width="122" height="118" fill="url(#sky1)"/></svg>
      <figcaption class="shot__caption">Lowering In 10” near Campbellton, TX.</figcaption>
    </figure>
    <figure class="shot" style="left:212px">
      <svg class="shot__photo" viewBox="0 0 122 118" role="img" aria-label="Photo of a 12-inch line along a right-of-way with a truck"><defs><linearGradient id="sky2" x1="0" y1="0" x2="0" y2="1"><stop offset="0" stop-color="#9dc0de"/><stop offset=".55" stop-color="#8a8f6a"/><stop offset="1" stop-color="#6c5b45"/></linearGradient></defs><rect width="122" height="118" fill="url(#sky2)"/></svg>
      <figcaption class="shot__caption">12” Line near Tilden, TX.</figcaption>
    </figure>
    <figure class="shot" style="left:374px">
      <svg class="shot__photo" viewBox="0 0 122 118" role="img" aria-label="Photo of pipe being placed by a yellow sideboom near the trench"><defs><linearGradient id="sky3" x1="0" y1="0" x2="0" y2="1"><stop offset="0" stop-color="#a8c6de"/><stop offset=".5" stop-color="#6f8a55"/><stop offset="1" stop-color="#3f3a30"/></linearGradient></defs><rect width="122" height="118" fill="url(#sky3)"/></svg>
      <figcaption class="shot__caption">12” Line near Tilden, TX.</figcaption>
    </figure>

    <div class="projects" style="top:404px">
      <h3 class="projects__heading">Project Management / Consulting</h3>
      <div>
        <div class="projects__row">Routing, Survey &amp; ROW Acquisition Coordination<em>for the installation of 6 miles of 12” through congested pipeline corridor near Corpus Christi, Texas (2014/15).</em></div>
        <div class="projects__row">Routing, Survey &amp; ROW Acquisition Coordination<em>for the installation of 60 miles of 12” pipeline in South Texas (2014).</em></div>
        <div class="projects__row">Routing, Survey &amp; ROW Acquisition Coordination<em>for the installation of 4 miles of 20” and 6” pipeline in Eastern Ohio (2013/14).</em></div>
        <div class="projects__row">Preliminary routing and AFE budget preparation<em>for 540 miles of pipeline across Colorado, Kansas, and Oklahoma (2014).</em></div>
        <div class="projects__row">Constructibility review and routing<em>for a 255 mile pipeline from Midland to Wichita Falls, Texas (2014).</em></div>
        <div class="projects__row">Constructibility review and FEED study assistance<em>for approximately 350 miles of 42” pipeline from near Monahans to the Texas/Mexico border (2014).</em></div>
        <div class="projects__row">Routing, Survey &amp; ROW Acquisition Coordination<em>for the installation of 4.5 miles of 16” and 6” pipeline in Eastern Ohio (2013).</em></div>
      </div>
    </div>

    <div class="projects" style="top:598px">
      <h3 class="projects__heading">Construction Management / Inspection</h3>
      <div>
        <div class="projects__row">Provide Construction Management and Inspection<em>for the installation of 30 miles of 12” pipeline through congested corridors near Houston, Texas (2014/15).</em></div>
        <div class="projects__row">Safety Inspection<em>for the installation of 58 miles of 12” pipeline in South Texas (2014).</em></div>
      </div>
    </div>

    <div class="projects" style="top:672px">
      <h3 class="projects__heading">Construction / Lump Sum Turnkey Projects</h3>
      <div>
        <div class="projects__row">Design and Installation of approximately 4,000 feet of 8” pipeline through “Refinery Row” near Corpus Christi.<em>Project included three (3) complex 8” HDDs (2014/15).</em></div>
        <div class="projects__row">Integrity replacements<em>on 8” pipeline through the Port of Corpus Christi industrial area (2014).</em></div>
      </div>
    </div>
  </section>

</main>
</body>
</html>
```